Fahrzeugbeschriftung für Cateringunternehmen
Zielgruppe
Wir werden ein neues Cateringunternehmen
Aufgabenstellung
Wir benötigen eine Fahrzeugwerbung (möglichst vollflächig) in einem edlen Design. Teil foliert würde auch gehen. Bitte angelehnt an unseren Firmenflyer, Texte bitte vom Flyer mit übernehmen, Fahrzeug ist ein Halvarin Torke Pelo 214 GTR/K/DUO (siehe Foto bei Dateiupload)

```html
<!DOCTYPE html>
<html lang="de">
<head>
<meta charset="utf-8">
<title>Fahrzeugbeschriftung – Tafelgut Elbtal</title>
<link rel="stylesheet" href="https://fonts.googleapis.com/css2?family=Arimo:ital,wght@0,700;1,700&family=Cinzel:wght@400;700&display=swap">
<style>
  :root {
    --canvas-bg: #f1f1ef;
    --body-white: #fbfbfa;
    --body-line: #c9cacb;
    --trim-dark: #3a3b3d;
    --glass: #2b2f33;
    --glass-light: #5d666c;
    --wood-dark: #2a1f17;
    --wood-mid: #4a3727;
    --gold: #c9a85c;
    --gold-light: #e6d29c;
    --text-dark: #151515;
    --tyre: #222324;
    --hubcap: #d9dadb;
  }
  html, body {
    margin: 0;
    padding: 0;
    width: 1200px;
    height: 845px;
    overflow: hidden;
    background: var(--canvas-bg);
  }
  .vehicle-wrap {
    display: block;
    width: 1200px;
    height: 845px;
  }
  .service-list {
    font-family: "Arimo", Arial, sans-serif;
    font-style: italic;
    font-weight: 700;
    font-size: 13px;
    fill: var(--text-dark);
  }
  .contact-address {
    font-family: "Arimo", Arial, sans-serif;
    font-weight: 700;
    font-size: 10px;
    fill: var(--text-dark);
  }
  .contact-phone {
    font-family: "Arimo", Arial, sans-serif;
    font-weight: 700;
    font-size: 17px;
    fill: var(--text-dark);
  }
  .contact-mail {
    font-family: "Arimo", Arial, sans-serif;
    font-weight: 700;
    font-size: 7px;
    fill: var(--text-dark);
  }
  .brand-name {
    font-family: "Cinzel", Georgia, serif;
    font-weight: 700;
    font-size: 21px;
    fill: var(--gold);
  }
  .brand-sub {
    font-size: 15px;
    letter-spacing: 2px;
  }
  .brand-web {
    font-family: "Cinzel", Georgia, serif;
    font-weight: 400;
    font-size: 11.5px;
    letter-spacing: 0.5px;
    fill: var(--gold);
  }
</style>
</head>
<body>
<svg class="vehicle-wrap" viewBox="0 0 1200 845" xmlns="http://www.w3.org/2000/svg">
  <defs>
    <linearGradient id="wood" x1="0" y1="0" x2="0" y2="1">
      <stop offset="0" stop-color="var(--wood-mid)"/>
      <stop offset="1" stop-color="var(--wood-dark)"/>
    </linearGradient>
    <linearGradient id="goldBand" x1="0" y1="0" x2="1" y2="0">
      <stop offset="0" stop-color="var(--gold)"/>
      <stop offset="0.6" stop-color="var(--gold-light)"/>
      <stop offset="1" stop-color="var(--gold)"/>
    </linearGradient>
    <radialGradient id="foodPlatter" cx="0.5" cy="0.5" r="0.6">
      <stop offset="0" stop-color="#c99a4a"/>
      <stop offset="0.6" stop-color="#6b4a2a"/>
      <stop offset="1" stop-color="#2c221a"/>
    </radialGradient>
    <radialGradient id="foodGlasses" cx="0.5" cy="0.5" r="0.6">
      <stop offset="0" stop-color="#b86a4a"/>
      <stop offset="0.6" stop-color="#5a4030"/>
      <stop offset="1" stop-color="#241c16"/>
    </radialGradient>
    <clipPath id="bodyClip">
      <path d="M64 630 L66 585 Q72 548 92 535 L262 473 Q350 410 452 360 Q520 352 700 350 L1071 358 Q1095 362 1102 376 L1126 500 L1130 655 L1130 672 L65 672 Z"/>
    </clipPath>
  </defs>

  <!-- body shell -->
  <g class="van-body">
    <path d="M64 630 L66 585 Q72 548 92 535 L262 473 Q350 410 452 360 Q520 352 700 350 L1071 358 Q1095 362 1102 376 L1126 500 L1130 655 L1130 672 L65 672 Z" fill="var(--body-white)" stroke="var(--body-line)" stroke-width="1.2"/>

    <g clip-path="url(#bodyClip)">
      <path class="gold-sweep" d="M300 602 Q700 590 1000 510 Q1070 488 1110 462 L1110 476 Q1060 505 1000 522 Q700 600 300 612 Z" fill="url(#goldBand)"/>
      <path class="wood-band" d="M300 612 Q700 600 1000 522 Q1060 505 1110 476 L1140 476 L1140 700 L300 700 Z" fill="url(#wood)"/>
      <path class="front-trim" d="M55 560 Q120 550 175 555 Q230 560 300 600 L300 700 L55 700 Z" fill="var(--trim-dark)"/>
      <path d="M1000 612 L1140 605 L1140 700 L1000 700 Z" fill="var(--trim-dark)"/>
    </g>

    <!-- windows -->
    <path class="windshield" d="M268 478 Q340 425 420 390 L395 440 L330 470 Z" fill="var(--glass)"/>
    <path class="front-window" d="M372 444 Q380 395 410 375 L548 372 L546 488 L362 494 Z" fill="var(--glass)"/>
    <path d="M385 440 Q395 405 418 395 L526 395 L526 484 L385 488 Z" fill="var(--glass-light)" opacity="0.55"/>
    <rect class="side-window" x="600" y="368" width="230" height="113" rx="6" fill="var(--glass)"/>
    <rect x="614" y="380" width="200" height="34" rx="4" fill="var(--glass-light)" opacity="0.45"/>
    <path d="M1103 485 L1122 488 L1124 560 L1104 562 Z" fill="#b4232a"/>
    <path d="M358 470 Q380 458 408 462 L410 496 L362 497 Z" fill="var(--trim-dark)"/>
    <path d="M85 545 Q130 528 185 524 L170 548 Q120 560 80 575 Z" fill="#9aa1a6"/>
    <line x1="576" y1="360" x2="578" y2="672" stroke="var(--body-line)" stroke-width="1.2"/>
    <line x1="353" y1="490" x2="355" y2="672" stroke="var(--body-line)" stroke-width="1.2"/>
    <line x1="838" y1="372" x2="838" y2="672" stroke="var(--body-line)" stroke-width="1.2"/>
    <rect x="505" y="501" width="55" height="8" rx="4" fill="var(--trim-dark)"/>
    <rect x="598" y="497" width="55" height="8" rx="4" fill="var(--trim-dark)"/>
  </g>

  <!-- wheels -->
  <g class="wheel">
    <circle cx="244" cy="672" r="70" fill="var(--tyre)"/>
    <circle cx="244" cy="672" r="47" fill="var(--hubcap)"/>
    <circle cx="244" cy="672" r="9" fill="#8c8e90"/>
  </g>
  <g class="wheel">
    <circle cx="931" cy="675" r="70" fill="var(--tyre)"/>
    <circle cx="931" cy="675" r="47" fill="var(--hubcap)"/>
    <circle cx="931" cy="675" r="9" fill="#8c8e90"/>
  </g>

  <!-- brand -->
  <g class="brand-badge">
    <circle cx="495" cy="589" r="74" fill="var(--wood-dark)" stroke="var(--gold)" stroke-width="3"/>
    <text class="brand-name" x="495" y="590" text-anchor="middle">TAFELGUT</text>
    <text class="brand-name brand-sub" x="495" y="616" text-anchor="middle">ELBTAL</text>
  </g>
  <text class="brand-web" x="640" y="609">TAFELGUT-ELBTAL.DE</text>

  <!-- contact -->
  <text class="contact-address" x="652" y="516" transform="rotate(-1.5 652 516)">Lindenweg 14 | 01099 Elbstadt</text>
  <text class="contact-phone" x="652" y="537" transform="rotate(-1.5 652 537)">0351-4418250</text>
  <text class="contact-mail" x="653" y="549" transform="rotate(-1.5 653 549)">info@tafelgut-elbtal.de</text>

  <!-- services -->
  <g class="service-list">
    <text x="838" y="405">•Taufe</text>
    <text x="838" y="421">•Kommunion</text>
    <text x="838" y="437">•Schuleinführung</text>
    <text x="838" y="453">•u.v.m. ...</text>
    <text x="957" y="405">•Hochzeiten</text>
    <text x="957" y="421">•Geburtstage</text>
    <text x="957" y="437">•Firmenevents</text>
    <text x="957" y="453">•Jugendweihe</text>
  </g>

  <!-- food photo circles -->
  <circle cx="910" cy="524" r="62" fill="url(#foodPlatter)" stroke="var(--body-white)" stroke-width="2" role="img" aria-label="Foto: Buffet mit Fingerfood-Häppchen auf Platten"/>
  <circle cx="1034" cy="524" r="43" fill="url(#foodGlasses)" stroke="var(--body-white)" stroke-width="2" role="img" aria-label="Foto: Dessertgläser und kleine Vorspeisen"/>
</svg>
</body>
</html>
```